Health Coach needs a Business Card Design

Need a really modern feminine business card design for a health and lifestyle coach. Needs to use geometric shapes, muted grey/blue/green pastels and black and white - see mood board attached and logo. The client likes black and white, modern, san serif with the use of lines and possibly a shadow leaf as in the mood board. Possibly put the tag line on the back or an icon of the logo. Logo is also attached. An icon of the logo would be great too.

Target Market(s)

Women (some men) aged 30 to 50.

Industry/Entity Type

Business

Contact Information for Business Card

Marla Teveny
e-mail: hello@marlatwell.example
website: marlatwell.example
Phone: +610497258316

The tag line is "Steady wellness, every day"

Font styles to use
Sans Serif

Colors
ecf7fb
cfeae6
000000
ffffff
f5f5f5

Requirements
Must have
• Black and white, logo, tag line and details
Nice to have
• Would be nice to incorporate the shadow palm.fern leaves as in the mood board and or geometric lines/shapes - see mood board. Could be either standard rectangle or would be happy with square too.
Should not have
• Flowers or decorations

```html
<!DOCTYPE html>
<html lang="en">
<head>
<meta charset="utf-8">
<title>Marla T — Business Card</title>
<link rel="stylesheet" href="https://fonts.googleapis.com/css2?family=Josefin+Sans:wght@300;400&display=swap">
<style>
  :root {
    --backdrop: #ececec;
    --mint: #cfeae6;
    --mint-deep: #b8e0da;
    --ice: #ecf7fb;
    --sky: #dbeef6;
    --paper: #f9f9f9;
    --stone: #e6e8e8;
    --ink: #555555;
    --ink-soft: #777777;
    --rule: #a9b3b2;
  }
  * { margin: 0; padding: 0; box-sizing: border-box; }
  html, body { width: 1200px; height: 900px; overflow: hidden; }
  body {
    background: var(--backdrop);
    font-family: "Josefin Sans", "Helvetica Neue", Arial, sans-serif;
    font-weight: 300;
    color: var(--ink);
    position: relative;
  }
  .card {
    position: absolute;
    width: 520px;
    height: 300px;
    overflow: hidden;
    box-shadow: 0 6px 18px rgba(0,0,0,0.10);
  }
  .card-shapes { position: absolute; inset: 0; }
  .card--front { left: 80px; top: 130px; background: var(--mint); }
  .card--back { left: 600px; top: 470px; background: var(--paper); }

  .brand { position: absolute; text-align: left; }
  .brand-name {
    font-weight: 300;
    color: var(--ink);
    letter-spacing: 0.04em;
    display: block;
    white-space: nowrap;
  }
  .brand-tagline {
    font-weight: 300;
    text-transform: uppercase;
    letter-spacing: 0.2em;
    color: var(--ink);
    display: block;
    white-space: nowrap;
  }
  .card--front .brand { left: 150px; top: 112px; }
  .card--front .brand-name { font-size: 40px; }
  .card--front .brand-tagline { font-size: 12px; margin-top: 8px; }

  .card--back .brand { left: 290px; top: 36px; }
  .card--back .brand-name { font-size: 26px; }
  .card--back .brand-tagline { font-size: 8px; margin-top: 5px; }

  .holder-name {
    position: absolute;
    left: 150px; top: 150px;
    font-size: 22px;
    font-weight: 300;
    letter-spacing: 0.22em;
    text-transform: uppercase;
    color: var(--ink);
    white-space: nowrap;
  }
  .contact-list { position: absolute; left: 150px; top: 192px; list-style: none; }
  .contact-item {
    display: flex; align-items: center; gap: 16px;
    height: 26px;
    font-size: 13px;
    letter-spacing: 0.14em;
    color: var(--ink-soft);
  }
  .contact-icon { width: 18px; height: 18px; flex: none; }
</style>
</head>
<body>

<section class="card card--front" aria-label="Card front">
  <svg class="card-shapes" viewBox="0 0 520 300" aria-hidden="true">
    <rect x="462" y="0" width="58" height="300" fill="var(--ice)"/>
    <rect x="440" y="40" width="1" height="220" fill="var(--rule)"/>
    <circle cx="72" cy="72" r="26" fill="none" stroke="var(--ice)" stroke-width="6"/>
    <rect x="60" y="226" width="34" height="34" fill="var(--ice)"/>
    <rect x="150" y="196" width="60" height="1" fill="var(--ink)"/>
  </svg>
  <div class="brand">
    <span class="brand-name">Marla T</span>
    <span class="brand-tagline">Steady wellness, every day</span>
  </div>
</section>

<section class="card card--back" aria-label="Card back">
  <svg class="card-shapes" viewBox="0 0 520 300" aria-hidden="true">
    <rect x="490" y="0" width="30" height="300" fill="var(--sky)"/>
    <rect x="468" y="0" width="10" height="300" fill="var(--mint)"/>
    <rect x="0" y="0" width="110" height="10" fill="var(--stone)"/>
    <rect x="118" y="150" width="1" height="120" fill="var(--rule)"/>
    <rect x="40" y="232" width="26" height="26" fill="var(--mint)"/>
    <circle cx="62" cy="90" r="30" fill="var(--stone)"/>
    <rect x="290" y="92" width="150" height="1" fill="var(--rule)"/>
  </svg>
  <div class="brand">
    <span class="brand-name">Marla T</span>
    <span class="brand-tagline">Steady wellness, every day</span>
  </div>
  <h1 class="holder-name">Marla Teveny</h1>
  <ul class="contact-list">
    <li class="contact-item">
      <svg class="contact-icon" viewBox="0 0 18 18" aria-hidden="true">
        <rect x="2" y="4" width="14" height="10" fill="none" stroke="var(--ink)" stroke-width="1"/>
        <path d="M2 4 L9 10 L16 4" fill="none" stroke="var(--ink)" stroke-width="1"/>
      </svg>
      <span>hello@marlatwell.example</span>
    </li>
    <li class="contact-item">
      <svg class="contact-icon" viewBox="0 0 18 18" aria-hidden="true">
        <circle cx="9" cy="9" r="7.5" fill="none" stroke="var(--ink)" stroke-width="1"/>
        <ellipse cx="9" cy="9" rx="3.5" ry="7.5" fill="none" stroke="var(--ink)" stroke-width="1"/>
        <path d="M1.5 9 H16.5 M3 5 H15 M3 13 H15" stroke="var(--ink)" stroke-width="1"/>
      </svg>
      <span>marlatwell.example</span>
    </li>
    <li class="contact-item">
      <svg class="contact-icon" viewBox="0 0 18 18" aria-hidden="true">
        <rect x="5" y="1.5" width="8" height="15" rx="1.5" fill="none" stroke="var(--ink)" stroke-width="1"/>
        <path d="M8 14 H10" stroke="var(--ink)" stroke-width="1"/>
      </svg>
      <span>+610497258316</span>
    </li>
  </ul>
</section>

</body>
</html>
```